Zielgruppe
Endkunde ist eine Immobilienfirma ((Bauträger)
Aufgabenstellung
Das Design soll für eine Präsentationsmappe erstellt werden und die Bemaßung sowie Farbigleit der vorgegebnen pdf-Datei beinhalten. Es soll in den Hausfarben , nebst den Backround in grau, gehalten werden.

```html
<!DOCTYPE html>
<html lang="de">
<head>
<meta charset="utf-8">
<title>Präsentationsmappe – Wohnwerk Elbtal AG</title>
<link href="https://fonts.googleapis.com/css2?family=Montserrat:wght@400;500;600&display=swap" rel="stylesheet">
<style>
  :root {
    --folder-grey: #5b5b5b;
    --stripe-grey: #c8c8c8;
    --paper: #ffffff;
    --brand-red: #8f2a21;
    --text-dark: #4a4a4a;
    --cut-pink: #e07aa8;
    --fold-blue: #2a8fb8;
    --rule-grey: #9a9a9a;
  }
  html, body { margin: 0; padding: 0; overflow: hidden; background: #ffffff; }
  .folder { display: block; width: 1200px; height: 883px; }
  .tagline { font-family: "Montserrat", sans-serif; font-weight: 500; font-size: 11.5px; fill: var(--paper); text-anchor: middle; letter-spacing: 0.2px; }
  .brand-name { font-family: "Montserrat", sans-serif; font-weight: 600; fill: var(--brand-red); }
  .address { font-family: "Montserrat", sans-serif; font-weight: 400; font-size: 9.6px; fill: var(--text-dark); text-anchor: middle; }
  .contact { font-family: "Montserrat", sans-serif; font-weight: 400; font-size: 10.5px; fill: var(--text-dark); text-anchor: middle; }
  .contact-light { font-family: "Montserrat", sans-serif; font-weight: 500; font-size: 13px; fill: var(--paper); text-anchor: middle; }
  .flap-contact { font-family: "Montserrat", sans-serif; font-weight: 400; font-size: 8.5px; fill: var(--paper); text-anchor: middle; }
  .cut-line { fill: none; stroke: var(--cut-pink); stroke-width: 0.8; }
  .cut-dashed { fill: none; stroke: var(--cut-pink); stroke-width: 0.7; stroke-dasharray: 3 3; }
  .fold-line { stroke: var(--fold-blue); stroke-width: 0.9; }
  .panel-rule { stroke: var(--rule-grey); stroke-width: 0.7; }
</style>
</head>
<body>
<svg class="folder" viewBox="0 0 1200 883" xmlns="http://www.w3.org/2000/svg">
  <defs>
    <linearGradient id="cover-photo-tones" x1="0" y1="0" x2="0" y2="1">
      <stop offset="0" stop-color="#e8dccb"/>
      <stop offset="0.45" stop-color="#dcdcd6"/>
      <stop offset="0.7" stop-color="#b9c48f"/>
      <stop offset="1" stop-color="#eeeeec"/>
    </linearGradient>
  </defs>

  <!-- Inner panel with tuck shape -->
  <path class="inner-panel" fill="var(--folder-grey)"
        d="M138 12 H675 V730 H151 L36 708 Q12 703 12 680 V52 Q12 40 26 36 Z"/>

  <!-- Cover panel -->
  <rect class="cover-panel" x="675" y="12" width="511" height="718" fill="var(--folder-grey)"/>

  <!-- White header bands -->
  <rect class="spine-band" x="12" y="105" width="126" height="143" fill="var(--paper)"/>
  <rect class="inner-band" x="150" y="105" width="513" height="143" fill="var(--paper)"/>
  <rect class="inner-band-gap" x="138" y="105" width="12" height="143" fill="var(--paper)"/>
  <rect class="inner-band-gap" x="663" y="105" width="12" height="143" fill="var(--paper)"/>
  <rect class="cover-band" x="675" y="105" width="511" height="143" fill="var(--paper)"/>

  <!-- Grey stripe -->
  <rect class="accent-stripe" x="2" y="248" width="1196" height="15" fill="var(--stripe-grey)"/>

  <!-- Panel separators -->
  <line class="panel-rule" x1="138" y1="105" x2="138" y2="263"/>
  <line class="panel-rule" x1="150" y1="105" x2="150" y2="263"/>
  <line class="panel-rule" x1="663" y1="105" x2="663" y2="263"/>
  <line class="fold-line" x1="675" y1="12" x2="675" y2="730"/>

  <!-- Taglines -->
  <text class="tagline" x="406" y="69">IHRE ZUFRIEDENHEIT, IST UNSERE MOTIVATION!</text>
  <text class="tagline" x="933" y="69">IHRE ZUFRIEDENHEIT, IST UNSERE MOTIVATION!</text>

  <!-- Spine marker -->
  <rect class="brand-square" x="54" y="155" width="34" height="34" fill="var(--brand-red)"/>

  <!-- Inner header: brand and address -->
  <g class="inner-brand">
    <text class="brand-name" x="420" y="156" font-size="15" text-anchor="end">Wohnwerk</text>
    <text class="brand-name" x="420" y="171" font-size="11" text-anchor="end">Elbtal AG</text>
    <rect class="brand-square" x="428" y="146" width="22" height="22" fill="var(--brand-red)"/>
  </g>
  <text class="address" x="390" y="195">Lindenhofweg 7 | 01468 Moritzdorf | Fon: 0351/40 62 18 75</text>
  <line class="panel-rule" x1="232" y1="198" x2="555" y2="198"/>
  <text class="address" x="390" y="209">Am Kirchberg 12 89540 Talfingen | Fon 07325 /44 21 09</text>
  <text class="contact" x="393" y="238">E-mail: kontakt@wwe-ag.de | Web: www.wwe-ag.de</text>

  <!-- Cover header brand -->
  <g class="cover-brand">
    <text class="brand-name" x="990" y="193" font-size="30" text-anchor="end">Wohnwerk</text>
    <text class="brand-name" x="990" y="223" font-size="23" text-anchor="end">Elbtal AG</text>
    <rect class="brand-square" x="1004" y="150" width="58" height="58" fill="var(--brand-red)"/>
  </g>

  <!-- Cover photo area -->
  <rect class="cover-photo" x="677" y="263" width="509" height="408" fill="url(#cover-photo-tones)"
        role="img" aria-label="Foto eines modernen weißen Einfamilienhauses mit Garten und Bauplanskizze im Vordergrund"/>

  <!-- Cover footer -->
  <text class="contact-light" x="935" y="703">E-mail: kontakt@wwe-ag.de | Web: www.wwe-ag.de</text>

  <!-- Bottom flap -->
  <path class="bottom-flap" fill="var(--folder-grey)"
        d="M151 730 H660 V742 L640 855 Q636 870 622 870 H277 L250 850 A42 42 0 0 1 182 790 L186 776 L151 742 Z"/>
  <line class="fold-line" x1="151" y1="730" x2="660" y2="730"/>
  <line class="fold-line" x1="151" y1="742" x2="660" y2="742"/>
  <g class="flap-brand" transform="rotate(180 425 800)">
    <text class="flap-contact" x="425" y="788">E-mail: kontakt@wwe-ag.de | Web: www.wwe-ag.de</text>
    <line x1="288" y1="806" x2="568" y2="806" stroke="#bdbdbd" stroke-width="0.7"/>
    <text class="brand-name" x="420" y="822" font-size="10" text-anchor="end" style="fill:#ffffff">Wohnwerk</text>
    <text class="brand-name" x="420" y="833" font-size="8" text-anchor="end" style="fill:#ffffff">Elbtal AG</text>
    <rect class="brand-square" x="426" y="815" width="16" height="16" fill="var(--brand-red)"/>
  </g>

  <!-- Cut and slit lines -->
  <path class="cut-line" d="M40 620 V632 L100 693 H112"/>
  <path class="cut-line" d="M475 755 A12 12 0 0 0 505 755"/>
  <path class="cut-line" d="M612 795 A14 14 0 0 0 612 818"/>
  <path class="cut-dashed" d="M138 12 H1186 V730 H675"/>
  <path class="cut-dashed" d="M12 105 V680"/>
</svg>
</body>
</html>
```